Brochure Design*

We are seeking a simple but powerful brochure design for our new company that uses electrostatic sprayers for the treatment and prevention of Covid 19 for businesses throughout the Southeast. The current brochure has too many photos and very distracting, i personally do not like anything about the brochure. Our sister company Harlow Print Supply was founded in 1983. Our company HPS Services LLC website is www.hpsvx.com
Updates

We need a few more days to receive feedback from our employees. Thank You

Target Market(s)

Business owners

Font styles to use
Serif
Sans Serif

Requirements
Must have
• A call for action brochure, simple while delivering a strong message
Should not have
• CLUTTER,

```html
<!DOCTYPE html>
<html lang="en">
<head>
<meta charset="utf-8">
<title>COVID-19 Safety Protection Flyer</title>
<link href="https://fonts.googleapis.com/css2?family=Cabin:wght@400;600;700&family=Oswald:wght@300;400&family=EB+Garamond:ital,wght@0,400;0,500;1,800&display=swap" rel="stylesheet">
<style>
  :root {
    --canvas: #e6e6e6;
    --paper: #ffffff;
    --green: #96c084;
    --icon-green: #8cbc7f;
    --blue: #3e67b1;
    --label-blue: #3a63b0;
    --dot-blue: #4a6fc0;
    --ink: #333333;
    --panel: rgba(140, 196, 205, 0.62);
  }
  * { margin: 0; padding: 0; box-sizing: border-box; }
  html, body { width: 1200px; height: 1200px; overflow: hidden; background: var(--canvas); }
  .flyer {
    position: absolute; left: 190px; top: 20px;
    width: 1000px; height: 1415px;
    transform: scale(0.82); transform-origin: 0 0;
    background: var(--paper);
    font-family: "Cabin", sans-serif;
  }
  .hero {
    position: absolute; left: 0; top: 0; width: 1000px; height: 545px;
    background: linear-gradient(180deg, #c9d6dc 0%, #9aa3a6 45%, #6c6c68 70%, #b9b2aa 100%);
  }
  .hero-panel {
    position: absolute; left: 312px; top: 0; width: 380px; height: 260px;
    background: var(--panel); color: #fff; text-align: center;
  }
  .hero-title { font-weight: 400; font-size: 74px; letter-spacing: 1px; line-height: 1; margin-top: 64px; }
  .hero-sub { font-weight: 400; font-size: 30px; line-height: 1; margin-top: 4px; letter-spacing: .5px; }
  .hero-lead { font-size: 19px; font-weight: 700; margin-top: 26px; }
  .hero-line { font-size: 18px; margin-top: 3px; }
  .sector {
    position: absolute; width: 300px; text-align: center;
    color: var(--label-blue); font-weight: 700; font-size: 22px; line-height: 28px;
  }
  .sector-icon {
    height: 64px; margin-bottom: 6px;
    display: flex; align-items: flex-end; justify-content: center;
  }
  .sector-icon svg { display: block; fill: var(--icon-green); }
  .row-one { top: 606px; }
  .row-two { top: 746px; }
  .info-band {
    position: absolute; left: 0; top: 893px; width: 1000px; height: 365px;
    background: var(--green); color: #fff;
  }
  .band-heading {
    position: absolute; font-family: "Oswald", sans-serif; font-weight: 300;
    font-size: 22px; letter-spacing: .5px; line-height: 32px; text-transform: uppercase;
  }
  .germ-icon { position: absolute; left: 318px; top: 22px; }
  .fact { position: absolute; left: 110px; width: 340px; font-family: "EB Garamond", serif; font-weight: 500; font-size: 18px; line-height: 22px; }
  .fact::before {
    content: ""; position: absolute; left: -52px; top: 7px;
    width: 12px; height: 12px; border-radius: 50%; background: var(--dot-blue);
  }
  .why-text { position: absolute; left: 515px; top: 114px; width: 460px; font-family: "EB Garamond", serif; font-weight: 500; font-size: 18px; line-height: 24px; }
  .cta {
    position: absolute; left: 516px; top: 230px; width: 380px; height: 91px;
    background: var(--blue); color: #fff; padding: 16px 0 0 38px;
    font-family: "EB Garamond", serif; font-style: italic; font-weight: 800; font-size: 25px; line-height: 30px;
  }
  .brand {
    position: absolute; left: 110px; top: 1322px;
    font-weight: 700; font-size: 22px; color: var(--icon-green);
    display: flex; align-items: center; gap: 8px;
  }
  .brand-mark { width: 14px; height: 14px; background: var(--icon-green); }
  .contact { position: absolute; left: 514px; font-size: 15px; color: var(--ink); }
  .contact svg { vertical-align: -4px; margin-right: 10px; }
</style>
</head>
<body>
<main class="flyer">
  <section class="hero" role="img" aria-label="Photo of two workers in white protective suits disinfecting large glass windows with sprayers">
    <div class="hero-panel">
      <h1 class="hero-title">COVID-19</h1>
      <p class="hero-sub">SAFETY PROTECTION</p>
      <p class="hero-lead">We ofter the best disinfection service.</p>
      <p class="hero-line">Protect yourself, Protect your client!</p>
    </div>
  </section>

  <div class="sector row-one" style="left:28px;">
    <div class="sector-icon"><svg width="64" height="58" viewBox="0 0 64 58"><rect x="22" y="0" width="20" height="10" rx="3" fill="none" stroke="#8cbc7f" stroke-width="4"/><rect x="0" y="8" width="64" height="50" rx="9"/><rect x="17" y="8" width="4" height="50" fill="#fff"/><rect x="43" y="8" width="4" height="50" fill="#fff"/></svg></div>
    Offices &amp; Bank
  </div>
  <div class="sector row-one" style="left:350px;">
    <div class="sector-icon"><svg width="54" height="62" viewBox="0 0 54 62"><path d="M2 0h28c0 14-6 22-12 24v30h10v5H4v-5h10V24C8 22 2 14 2 0z"/><path d="M38 0h3v16h3V0h3v16h3V0h3v18c0 4-3 6-5 7v37h-5V25c-2-1-5-3-5-7z"/></svg></div>
    Dining Room
  </div>
  <div class="sector row-one" style="left:681px;">
    <div class="sector-icon"><svg width="66" height="58" viewBox="0 0 66 58"><rect x="0" y="22" width="6" height="20" rx="2"/><rect x="8" y="14" width="12" height="34" rx="2"/><rect x="20" y="27" width="26" height="8"/><rect x="46" y="14" width="12" height="34" rx="2"/><rect x="60" y="22" width="6" height="20" rx="2"/></svg></div>
    Fitness Centre
  </div>
  <div class="sector row-two" style="left:28px;">
    <div class="sector-icon"><svg width="80" height="58" viewBox="0 0 80 58"><rect x="24" y="0" width="32" height="56"/><circle cx="40" cy="13" r="9" fill="#fff"/><rect x="38" y="7" width="4" height="12"/><rect x="34" y="11" width="12" height="4"/><rect x="4" y="16" width="18" height="40"/><rect x="58" y="16" width="18" height="40"/><rect x="35" y="38" width="10" height="18" fill="#fff"/><rect x="0" y="54" width="80" height="4"/></svg></div>
    Medical Facility
  </div>
  <div class="sector row-two" style="left:350px;">
    <div class="sector-icon"><svg width="68" height="48" viewBox="0 0 68 48"><path d="M0 6h68l-10 10v10c-8 4-40 4-48 0V16z"/><rect x="62" y="10" width="2" height="22"/><path d="M60 32h6l-3 10z"/></svg></div>
    School &amp; Day Care
  </div>
  <div class="sector row-two" style="left:681px;">
    <div class="sector-icon"><svg width="58" height="58" viewBox="0 0 58 58"><path d="M6 4l10-2 7 14-7 6c3 8 10 15 18 18l6-7 14 7-2 10c-2 4-8 6-14 4C21 48 8 35 2 19 0 12 2 6 6 4z"/><path d="M34 10a14 14 0 0 1 14 14" fill="none" stroke="#8cbc7f" stroke-width="4"/><path d="M36 0a22 22 0 0 1 22 22" fill="none" stroke="#8cbc7f" stroke-width="4"/><circle cx="36" cy="22" r="4"/></svg></div>
    Data Centre
  </div>

  <section class="info-band">
    <h2 class="band-heading" style="left:109px; top:36px;">How long do germs<br>stay on surfaces?</h2>
    <svg class="germ-icon" width="82" height="82" viewBox="0 0 82 82" aria-hidden="true">
      <g stroke="#3e67b1" stroke-width="3" stroke-linecap="round">
        <line x1="41" y1="2" x2="41" y2="80"/><line x1="2" y1="41" x2="80" y2="41"/>
        <line x1="13" y1="13" x2="69" y2="69"/><line x1="69" y1="13" x2="13" y2="69"/>
        <line x1="26" y1="5" x2="56" y2="77"/><line x1="56" y1="5" x2="26" y2="77"/>
        <line x1="5" y1="26" x2="77" y2="56"/><line x1="5" y1="56" x2="77" y2="26"/>
      </g>
      <circle cx="41" cy="41" r="27" fill="#3e67b1"/>
      <g fill="#7ea3e0"><circle cx="32" cy="32" r="4"/><circle cx="50" cy="36" r="3"/><circle cx="40" cy="50" r="4"/><circle cx="28" cy="47" r="2.5"/><circle cx="53" cy="50" r="2.5"/></g>
    </svg>
    <p class="fact" style="top:122px;">SARS-CoV-2 can remain on surfaces<br>for hours and up to 9 days.</p>
    <p class="fact" style="top:185px;">Microorganisms can survive on surfaces<br>for days, weeks, and even months</p>
    <p class="fact" style="top:247px;">Electrostatic technology is one of the most<br>effective method in eliminating pathogen.</p>

    <h2 class="band-heading" style="left:515px; top:62px;">Why do you need disinfection?</h2>
    <p class="why-text">Let your visitors know that you care about their health.<br>We will place a decal on your door/window to let them know<br>that your place of business has been thoroughly disinfected.</p>
    <p class="cta">We will give your business<br>a "Certified Clean".</p>
  </section>

  <div class="brand"><span class="brand-mark"></span>Kestrel Clean Co.</div>
  <p class="contact" style="top:1320px;">415 Linden Court, Cary, North Carolina 27511</p>
  <p class="contact" style="top:1351px;">
    <svg width="16" height="16" viewBox="0 0 16 16"><path d="M2 1l3-1 2 4-2 2c1 2 3 4 5 5l2-2 4 2-1 3c-1 1-3 2-5 1C6 13 3 10 1 6 0 4 1 2 2 1z" fill="none" stroke="#3e67b1" stroke-width="1.3"/></svg>1-800-555-0142
    <span style="margin-left:60px;"><svg width="16" height="16" viewBox="0 0 16 16"><g fill="none" stroke="#3e67b1" stroke-width="1.2"><circle cx="8" cy="8" r="7"/><ellipse cx="8" cy="8" rx="3" ry="7"/><line x1="1" y1="8" x2="15" y2="8"/></g></svg>www.kestrelcleanco.com</span>
  </p>
</main>
</body>
</html>
```